Home Page Website Design

The Site width is 1000 px. I've attached a Balsamiq mockup as a design layout guide. The design needs to be flat and clean. Please stick to the pixel dimensions of the mock up as the site will be responsive. I've also attached the logos used on the mockup for positional purposes.

Colours to use: Black, Grey, Green (Logo tie in) & green complementary colours.

Green (Logo tie in)
White Background
Titles: Black (Roboto Bold 700)
Text: Dark Grey (Roboto Normal 400)

Look & Style Example
http://www.brindlowlearn.org.uk/

Type Face
Google Fonts - Roboto

These are just guidelines, please feel free to use you own creative judgment.

Thanks

```html
<!DOCTYPE html>
<html lang="en">
<head>
<meta charset="utf-8">
<title>Brindlow Teaching School Alliance – Home</title>
<link href="https://fonts.googleapis.com/css2?family=Roboto:wght@400;500;700&family=Roboto+Condensed:wght@400;700&display=swap" rel="stylesheet">
<style>
:root{
  --green:#05b04a;
  --green-soft:#7fd39c;
  --green-pale:#b9e6c6;
  --ink:#222;
  --text:#666;
  --grey-bar:#4a4c4f;
  --grey-dark:#3c3e41;
  --panel:#f3f3f3;
  --panel-line:#dedede;
  --white:#fff;
}
*{box-sizing:border-box;margin:0;padding:0}
html,body{width:1057px;height:1200px;overflow:hidden;background:var(--white);font-family:"Roboto",sans-serif;color:var(--text)}
.canvas{position:relative;width:1057px;height:1200px}
.abs{position:absolute}

/* header */
.brand{left:160px;top:24px;display:flex;align-items:center;gap:8px;color:var(--green);font-weight:500;font-size:13px;line-height:1.25}
.brand-mark{width:22px;height:22px;background:var(--green)}
.login{left:838px;top:16px;width:57px;height:19px;background:var(--grey-bar);color:#fff;font-size:7.5px;display:flex;align-items:center;justify-content:center;border-radius:2px}
.chat{left:546px;top:59px;width:102px;height:40px;border:1px solid var(--panel-line);display:flex;align-items:center;gap:6px;padding-left:10px;color:var(--green);font-family:"Roboto Condensed",sans-serif;font-weight:700;font-size:9px}
.register{left:657px;top:43px;width:240px;height:57px;border:1px solid var(--panel-line);padding:9px 13px}
.register h3{color:var(--green);font-family:"Roboto Condensed",sans-serif;font-size:11px;font-weight:700}
.register .row{display:flex;gap:6px;margin-top:6px}
.register .field{width:155px;height:18px;border:1px solid var(--panel-line);font-size:6px;padding:5px 9px;color:#999}
.register .submit{width:57px;height:18px;background:var(--green);color:#fff;font-size:7px;display:flex;align-items:center;justify-content:center}

/* nav */
.nav{left:159px;top:111px;width:740px;height:35px;background:var(--grey-bar);border-bottom:3px solid var(--green);display:flex;align-items:center;padding-left:22px}
.nav a{color:#fff;text-decoration:none;font-family:"Roboto Condensed",sans-serif;font-size:8px;margin-right:24px}
.search{position:absolute;right:8px;top:7px;width:142px;height:17px;background:var(--grey-dark);border:1px solid #555;font-size:6px;color:#bbb;padding:4px 8px}
.search svg{position:absolute;right:5px;top:3px}

/* hero */
.hero-copy{left:159px;top:154px;width:246px;height:283px;background:var(--green);color:#fff;padding:27px 22px}
.hero-copy h1{font-family:"Roboto Condensed",sans-serif;font-weight:700;font-size:24px;line-height:1}
.hero-copy h2{font-family:"Roboto Condensed",sans-serif;font-weight:700;font-size:14.5px;margin:4px 0 18px 3px}
.hero-copy p{font-size:7.8px;line-height:13.6px;margin-bottom:13px;letter-spacing:-.1px}
.btn-more{display:inline-block;margin-top:3px;width:115px;height:28px;background:#eee;color:#555;font-family:"Roboto Condensed",sans-serif;font-size:10px;line-height:28px;text-align:center;border-radius:2px}
.dots{position:absolute;right:12px;bottom:12px;display:flex;gap:3px}
.dots span{width:9px;height:9px;border-radius:50%;background:#2fc068}
.hero-photo{left:405px;top:154px;width:494px;height:283px;background:linear-gradient(120deg,#3a3b3d 0%,#c9c5c0 40%,#eae7e3 70%,#b8b4ae 100%)}

/* sections */
.sec-title{top:457px;font-family:"Roboto Condensed",sans-serif;font-weight:700;font-size:13px;color:var(--ink)}
.panel{background:var(--panel);border:1px solid var(--panel-line)}
.welcome{left:159px;top:484px;width:235px;height:364px;padding:10px}
.video{width:214px;height:128px;background:linear-gradient(135deg,#5a6f86,#cdd5de 55%,#43505e);position:relative}
.video-bar{position:absolute;left:0;right:0;bottom:0;height:11px;background:#e9e9e9;font-size:5px;color:#333;display:flex;align-items:center;gap:5px;padding:0 5px}
.video-bar i{flex:1;height:3px;background:#bbb}
.welcome p{font-size:7.4px;line-height:14.4px;margin:24px 6px 0 6px}
.welcome p+p{margin-top:14px}

.training{left:411px;top:484px;width:235px;height:163px;padding:12px 10px}
.track{height:25px;background:var(--grey-bar);border-bottom:2px solid var(--green);color:#fff;font-family:"Roboto Condensed",sans-serif;font-size:8px;display:flex;align-items:center;justify-content:space-between;padding:0 10px 0 13px;margin-bottom:4px}
.news{left:411px;top:686px;width:235px;height:162px;padding:12px 20px}
.news-item h4{font-size:9.5px;font-weight:400;color:var(--ink);margin-bottom:6px}
.news-item p{font-size:7px;line-height:14.4px}
.news-item+.news-item{border-top:1px solid var(--panel-line);margin-top:9px;padding-top:10px}

.courses{left:664px;top:484px;width:235px;height:364px;padding:0 16px 0 16px;overflow:hidden}
.course{padding:16px 0 10px;border-bottom:1px solid var(--panel-line)}
.course h4{font-size:10.5px;font-weight:400;color:var(--ink);line-height:17.6px}
.course p{font-size:7px;line-height:14.4px;margin-top:5px}
.course .foot{display:flex;justify-content:space-between;align-items:center;margin-top:5px}
.course em{font-size:7.5px;color:var(--green);font-weight:500}
.book{width:53px;height:16px;background:var(--green);color:#fff;font-size:7.5px;display:flex;align-items:center;justify-content:center}
.scroll{position:absolute;right:4px;top:8px;width:4px;height:348px}
.scroll b{display:block;width:4px;height:60px;margin-top:10px;background:#555}

/* footer */
.footer{left:159px;top:870px;width:740px;height:140px;background:var(--green);color:#fff}
.footer .addr{position:absolute;left:29px;top:20px;font-size:8.6px;line-height:16px}
.footer .addr .contact{display:flex;align-items:center;gap:6px;font-size:7.5px;margin-top:5px}
.footer ul{position:absolute;list-style:none;font-size:8.6px;line-height:18px;top:18px}
.social{position:absolute;left:553px;top:24px;display:flex;gap:18px;font-size:8.6px}
.social span{display:flex;align-items:center;gap:6px}
.social i{width:18px;height:18px;border-radius:3px;background:#fff;opacity:.85}
.award{position:absolute;left:558px;top:60px;width:126px;height:59px;background:var(--green-soft)}

/* partners */
.partners-title{left:0;width:1057px;top:1026px;text-align:center;font-family:"Roboto Condensed",sans-serif;font-weight:700;font-size:13px;color:var(--ink)}
.partners{left:159px;top:1052px;width:740px;height:68px;border:1px solid var(--panel-line);display:flex;align-items:center;justify-content:space-around;padding:0 8px}
.partners span{display:block;background:#d6dbe2}
.copyright{left:159px;top:1134px;width:740px;height:25px;background:#ececec;font-size:6.8px;color:#888;display:flex;align-items:center;justify-content:center}
</style>
</head>
<body>
<div class="canvas">

  <div class="abs brand"><span class="brand-mark"></span><span>Brindlow Teaching<br>School Alliance</span></div>
  <div class="abs login">LOGIN</div>
  <div class="abs chat">
    <svg width="22" height="22" viewBox="0 0 22 22"><circle cx="11" cy="10" r="9" fill="#f4c232"/><circle cx="14" cy="14" r="6" fill="#3aa4e0"/></svg>
    LIVE CHAT
  </div>
  <div class="abs register">
    <h3>REGISTER NOW</h3>
    <div class="row"><div class="field">EMAIL ADDRESS :</div><div class="submit">SUBMIT</div></div>
  </div>

  <nav class="abs nav">
    <a>HOME</a><a>ABOUT US</a><a>TRAINING &amp; DEVELOPMENT</a><a>BENEFITS</a><a>MEMBERS</a><a>WHAT'S ON</a><a>CONTACT US</a><a>NEWS</a><a>FOURM</a>
    <div class="search">SEARCH :
      <svg width="10" height="10" viewBox="0 0 10 10"><circle cx="4" cy="4" r="3" fill="none" stroke="#999" stroke-width="1.2"/><line x1="6.2" y1="6.2" x2="9" y2="9" stroke="#999" stroke-width="1.4"/></svg>
    </div>
  </nav>

  <section class="abs hero-copy">
    <h1>NEW TEACHERS</h1>
    <h2>IN WORKSHOP</h2>
    <p>lorem ipsum dolor st amet, consectetur adipscing elit, sed eiusmod tenpor incididunt labore et dolore mogna oliqua Ut erim od minim venrom, quis nostrud exercitabon ullamco labors ns up ex eaexercitabon ullamco labors ns up ex ea comm. consequot Duis oute tugtot nulla pariatur Excepteur..</p>
    <p>ortiet, consectetur adipiscing elit, sedsmod terrpor incididunt ut laCore et dolore...</p>
    <span class="btn-more">FIND OUT MORE</span>
    <div class="dots"><span></span><span></span></div>
  </section>
  <div class="abs hero-photo" role="img" aria-label="Photo of three colleagues shaking hands across an office desk"></div>

  <h2 class="abs sec-title" style="left:160px">WELCOME</h2>
  <h2 class="abs sec-title" style="left:412px">TRAINING &amp; DEVELOPMENT</h2>
  <h2 class="abs sec-title" style="left:665px">LATEST COURSES</h2>
  <h2 class="abs sec-title" style="left:412px;top:660px">NEWS</h2>

  <section class="abs panel welcome">
    <div class="video" role="img" aria-label="Video still of colleagues meeting around a table">
      <svg style="position:absolute;left:93px;top:44px" width="28" height="28" viewBox="0 0 28 28"><circle cx="14" cy="14" r="13" fill="rgba(255,255,255,.35)"/><path d="M11 8 L20 14 L11 20Z" fill="rgba(255,255,255,.8)"/></svg>
      <div class="video-bar"><span>▶</span><span>00:00</span><i></i><span>00:00</span></div>
    </div>
    <p>Lorem Ipsum is simply dummy text of the printing and typesetting industry. Lorem Ipsum has been the industry's standard dummy text ever since the 1500s, when an unknown printer took a galley of type and scrambled it to make a type specimen book. unknown printer took a galley of type and scrambled it to make a type specimen book. s survived not only five centuries, but also the leap into electronic typesetting, remaining essentially unchanged...</p>
    <p>It has survived not only five centuries, unknown printer took a galley of type and scrambled it to make a type specimen book. but also the leap into electronic typesetting, remaining essentially unchanged...</p>
  </section>

  <section class="abs panel training">
    <div class="track">LEADERSHIP TRAINING<span>›</span></div>
    <div class="track">CPD<span>›</span></div>
    <div class="track">SCHOOL 2 SCHOOL SUPPORT<span>›</span></div>
    <div class="track">RESEARCH &amp; DEVELOPMENT<span>›</span></div>
    <div class="track">ITT ( SCHOOL DIRECT )<span>›</span></div>
  </section>

  <section class="abs panel news">
    <div class="news-item"><h4>Lorem Ipsum is simply dummy</h4><p>Lorem Ipsum is simply dummy text of the printing and typesetting industry. Lorem Ipsum has been the industry's standard dummy text ever since the 1500s...</p></div>
    <div class="news-item"><h4>Lorem Ipsum is simply dummy</h4><p>Lorem Ipsum is simply dummy text of the printing and typesetting industry. Lorem Ipsum has been the industry's standard dummy text ever since the 1500s...</p></div>
  </section>

  <section class="abs panel courses">
    <div class="course"><h4>Want to deliver consistently outstanding Lessons?</h4><p>Lorem Ipsum is simply dummy text of the printing and typesetting industry the industry's standard...</p><div class="foot"><em>6 places Left</em><span class="book">Book</span></div></div>
    <div class="course"><h4>Want to deliver consistently outstanding Lessons?</h4><p>Lorem Ipsum is simply dummy text of the printing and typesetting industry the industry's standard...</p><div class="foot"><em>6 places Left</em><span class="book">Book</span></div></div>
    <div class="course" style="border:0"><h4>Want to deliver consistently outstanding Lessons?</h4><p>Lorem Ipsum is simply dummy text of the printing and typesetting industry the industry's standard...</p><div class="foot"><em>6 places Left</em><span class="book">Book</span></div></div>
    <div class="scroll"><b></b></div>
  </section>

  <footer class="abs footer">
    <div class="addr">
      Brindlow Teaching Schools Alliance,<br>Harrow Lane,<br>Brindlow
      <div class="contact" style="margin-top:8px"><svg width="12" height="12" viewBox="0 0 12 12"><path d="M3 1h3l1 3-2 1c.6 1.4 1.6 2.4 3 3l1-2 3 1v3c-6 0-9-3-9-9z" fill="#fff"/></svg>Tel : 01632 960412</div>
      <div class="contact"><svg width="12" height="10" viewBox="0 0 12 10"><rect x="1" y="1" width="10" height="8" fill="none" stroke="#fff"/><path d="M1 1l5 4 5-4" fill="none" stroke="#fff"/></svg>Email : info@brindlowlearn.org.uk</div>
    </div>
    <ul style="left:270px"><li>About Us</li><li>Ironing &amp; Development</li><li>Benefits</li><li>Members</li><li>Cdendor ot Events</li></ul>
    <ul style="left:451px"><li>Contact us</li><li>News</li><li>Forum</li><li>Site Map</li></ul>
    <div class="social"><span><i></i>Circlebook</span><span><i></i>Chirper</span></div>
    <div class="award" role="img" aria-label="Accreditation badge"></div>
  </footer>

  <h2 class="abs partners-title">PARTNERS SCHOOL</h2>
  <div class="abs partners" aria-label="Partner school badges">
    <span style="width:32px;height:36px;border-radius:50%"></span>
    <span style="width:70px;height:36px"></span>
    <span style="width:80px;height:24px"></span>
    <span style="width:22px;height:46px"></span>
    <span style="width:24px;height:42px"></span>
    <span style="width:32px;height:46px"></span>
    <span style="width:42px;height:46px;border-radius:50%"></span>
    <span style="width:41px;height:43px"></span>
    <span style="width:100px;height:46px"></span>
    <span style="width:66px;height:40px"></span>
    <span style="width:63px;height:26px"></span>
  </div>

  <div class="abs copyright">© Brindlow Teaching Schools Alliance</div>
</div>
</body>
</html>
```